Qarnetix EIRL Business Card Design Project

We need a business card design for a New Business Intelligence Consultant. We bring a complete service to the client from first consulting meeting to help desk and system improvement.

I will upload the company logo and I like to use the logo colors on the card. Feel free to use all logo components on the design, for example one side with the black logo using complete card and the other side only the red shape (is an example, feel absolutely free :)).

The principal idea is to sell a professional service and a modern company.

Target Market(s)

IT Business Intelligence Clients

Industry/Entity Type

Professional Service

Requirements
Nice to have
• - Use the logo colors and minimize white sections.
- Rounded borders
Should not have
• I don't want to see any references to people working on a meeting or office photos or any computers related logos.

```html
<!DOCTYPE html>
<html lang="es">
<head>
<meta charset="utf-8">
<title>Qarnetix EIRL – Tarjeta de presentación</title>
<link rel="stylesheet" href="https://fonts.googleapis.com/css2?family=Arimo:wght@400;700&family=Cousine:wght@400&display=swap">
<style>
  :root {
    --bg: #d9d9d9;
    --card-black: #1f1f1f;
    --card-white: #ffffff;
    --brand-red: #e0211f;
    --brand-gray: #8c8c8c;
    --text-dark: #2b2b2b;
    --text-light: #f2f2f2;
    --text-muted: #cfcfcf;
  }
  * { box-sizing: border-box; margin: 0; padding: 0; }
  html, body { width: 1200px; height: 951px; overflow: hidden; }
  body {
    background: var(--bg);
    position: relative;
    font-family: "Arimo", Arial, sans-serif;
  }
  .card {
    position: absolute;
    border-radius: 26px;
    overflow: hidden;
    box-shadow: 0 10px 28px rgba(0,0,0,0.25);
  }
  /* Back side */
  .card--back {
    left: 70px; top: 110px;
    width: 560px; height: 315px;
    background: var(--card-black);
    display: flex; align-items: center; justify-content: center; gap: 18px;
  }
  .back-mark {
    width: 26px; height: 26px;
    background: var(--brand-red);
  }
  .back-name {
    font-weight: 700;
    font-size: 64px;
    color: var(--brand-gray);
    letter-spacing: 1px;
  }
  /* Front side */
  .card--front {
    left: 540px; top: 490px;
    width: 600px; height: 338px;
    background: var(--card-white);
  }
  .front-shape { position: absolute; inset: 0; width: 100%; height: 100%; }
  .brand {
    position: absolute; left: 34px; top: 54px;
    display: flex; align-items: center; gap: 10px;
  }
  .brand-square { width: 28px; height: 28px; background: var(--brand-gray); }
  .brand-name {
    font-weight: 700; font-size: 38px; line-height: 1;
    color: var(--brand-red);
  }
  .contact {
    position: absolute; left: 18px; top: 122px;
    font-family: "Cousine", "Courier New", monospace;
    font-size: 14px; line-height: 17px;
    color: var(--text-dark);
    list-style: none;
  }
  .contact-item { display: flex; align-items: flex-start; gap: 10px; }
  .contact-item--address { margin-bottom: 22px; }
  .contact-icon { width: 14px; height: 14px; flex: none; margin-top: 2px; fill: var(--brand-red); }
  .person {
    position: absolute; left: 375px; top: 180px;
    width: 210px; text-align: center;
  }
  .person-name { font-size: 21px; color: var(--text-light); }
  .person-title { font-size: 14px; color: var(--text-muted); margin-top: 3px; }
</style>
</head>
<body>

<section class="card card--back" aria-label="Reverso de la tarjeta">
  <span class="back-mark"></span>
  <span class="back-name">qarnetix</span>
</section>

<section class="card card--front" aria-label="Anverso de la tarjeta">
  <svg class="front-shape" viewBox="0 0 600 338" preserveAspectRatio="none" aria-hidden="true">
    <path d="M345,0 C307,100 297,230 337,338 L600,338 L600,0 Z" fill="#1f1f1f"/>
    <path d="M313,0 C271,100 269,240 317,338 L337,338 C297,230 307,100 345,0 Z" fill="#e0211f"/>
    <path d="M297,0 C257,110 259,240 303,338" fill="none" stroke="#e0211f" stroke-width="2"/>
  </svg>

  <div class="brand">
    <span class="brand-square"></span>
    <span class="brand-name">qarnetix</span>
  </div>

  <ul class="contact">
    <li class="contact-item contact-item--address">
      <svg class="contact-icon" viewBox="0 0 14 14"><path d="M7 1 L13 7 H11 V13 H8 V9 H6 V13 H3 V7 H1 Z"/></svg>
      <span>Av. Los Aromos 418,<br>Of. 305, Providencia,<br>Santiago, Chile</span>
    </li>
    <li class="contact-item">
      <svg class="contact-icon" viewBox="0 0 14 14"><path d="M3 1 L5.5 1 L6.5 4 L5 5.3 C5.8 7 7 8.2 8.7 9 L10 7.5 L13 8.5 L13 11 C13 12 12 13 11 13 C6 13 1 8 1 3 C1 2 2 1 3 1 Z"/></svg>
      <span>+56 (9) 84210957</span>
    </li>
    <li class="contact-item">
      <svg class="contact-icon" viewBox="0 0 14 14"><path d="M1 3 H13 V11 H1 Z M1.5 3.5 L7 8 L12.5 3.5" stroke="#fff" stroke-width="1"/></svg>
      <span>tomas@qarnetix.cl</span>
    </li>
    <li class="contact-item">
      <svg class="contact-icon" viewBox="0 0 14 14"><circle cx="7" cy="7" r="6"/></svg>
      <span>www.qarnetix.cl</span>
    </li>
  </ul>

  <div class="person">
    <p class="person-name">Tomás Alarcón</p>
    <p class="person-title">Gerente General</p>
  </div>
</section>

</body>
</html>
```